K & M Tire Shop business cards

need business card for tire/car care company based in tampa, florida. we sell used and new tires, also we service vehicles, tune ups, oil chasnge, brakes and A/c we offer free towing with major vehicle repair and tire purchase. we also offer free estimates on any engine or a/c repair. also we have the lowest price in the city on used and new tires.

Industry/Entity Type

Business

Contact Information for Business Card

4187 N Crestwell Ave,
Tampa, Fl 33829
Ph: 813-572-6148
KandMTireShop@examplemail.com

Font styles to use
Serif
Sans Serif
Decorative

Requirements
Must have
• my logo, what we do ( used and new tires , oil change, brakes, tune ups, free towing vehicl. Also business info.
Nice to have
• an image of a towing truck, highlighting that we offer free towing. something close to what i have in one of the attached image

```html
<!DOCTYPE html>
<html lang="en">
<head>
<meta charset="utf-8">
<title>K &amp; M Tire Shop – Business Cards</title>
<link rel="stylesheet" href="https://fonts.googleapis.com/css2?family=Bebas+Neue&display=swap">
<style>
  :root {
    --page-bg: #ffffff;
    --card-deep: #062b45;
    --card-mid: #0b4a6e;
    --card-glow: #1a86ab;
    --accent-yellow: #f4e21a;
    --text-white: #ffffff;
    --truck-body: #d9dee3;
    --truck-shadow: #5a6b78;
  }
  * { margin: 0; padding: 0; box-sizing: border-box; }
  html, body {
    width: 1200px;
    height: 1000px;
    overflow: hidden;
    background: var(--page-bg);
  }
  .canvas {
    position: relative;
    width: 1200px;
    height: 1000px;
    font-family: "Bebas Neue", "Arial Narrow", sans-serif;
  }
  .card {
    position: absolute;
    left: 353px;
    width: 496px;
    height: 289px;
    overflow: hidden;
    background:
      radial-gradient(ellipse 60% 70% at 50% 55%, var(--card-glow) 0%, var(--card-mid) 45%, var(--card-deep) 100%);
  }
  .card--front { top: 181px; }
  .card--back  { top: 528px; }

  .card--front {
    background:
      radial-gradient(ellipse 40% 55% at 22% 40%, var(--card-glow) 0%, var(--card-mid) 50%, transparent 100%),
      linear-gradient(160deg, var(--card-mid) 0%, var(--card-deep) 100%);
  }

  .brand-name {
    position: absolute;
    color: var(--accent-yellow);
    font-weight: 400;
    white-space: nowrap;
    letter-spacing: 0.5px;
  }
  .card--front .brand-name {
    left: 28px;
    top: 72px;
    font-size: 34px;
  }
  .card--back .brand-name {
    left: 0;
    right: 0;
    top: 127px;
    text-align: center;
    font-size: 52px;
  }

  .offer-headline {
    position: absolute;
    left: 251px;
    top: 21px;
    color: var(--text-white);
    font-size: 24px;
    line-height: 31px;
    letter-spacing: 0.8px;
  }
  .offer-headline .highlight { color: var(--accent-yellow); }

  .tow-truck-image {
    position: absolute;
    left: 255px;
    top: 84px;
    width: 218px;
    height: 106px;
    border-radius: 6px;
    background: radial-gradient(ellipse 60% 55% at 55% 50%, var(--truck-body) 0%, var(--truck-shadow) 65%, transparent 100%);
  }

  .contact-details {
    position: absolute;
    left: 252px;
    top: 201px;
    list-style: none;
    color: var(--text-white);
    font-size: 13.5px;
    line-height: 18.3px;
    letter-spacing: 0.5px;
  }
  .contact-details .label { color: var(--accent-yellow); }
</style>
</head>
<body>
<main class="canvas">

  <section class="card card--front" aria-label="Business card front">
    <div class="brand-name">K &amp; M Tire Shop</div>

    <h1 class="offer-headline">
      <span class="highlight">Free</span> towing with major<br>
      repair or tire service.
    </h1>

    <div class="tow-truck-image" role="img" aria-label="Photo of a white flatbed tow truck"></div>

    <ul class="contact-details">
      <li>4187 N Crestwell Ave</li>
      <li>Tampa, FL 33829</li>
      <li><span class="label">P:</span> 813-572-6148</li>
      <li><span class="label">E:</span> KandMTireShop@examplemail.com</li>
    </ul>
  </section>

  <section class="card card--back" aria-label="Business card back">
    <div class="brand-name">K &amp; M Tire Shop</div>
  </section>

</main>
</body>
</html>
```